Business Card Design

We are looking for a business card designed for our landscaping company. We do landscaping installation & Maintenance Services. We would like to see designs that have basic landscaping in background. We also think it is important to have both of our names and phone numbers on the card. We need something that stands out a little whether it is shape of the card or thickness or design.

Industry/Entity Type

Business

Contact Information for Business Card

Pale Ridge Yardworks, paleridgeyardworks@mailbrook.net, Dale Purvine 555-213-7690, Martin Kolbey 555-864-1037

```html
<!DOCTYPE html>
<html lang="en">
<head>
<meta charset="utf-8">
<title>Pale Ridge Yardworks – Business Card</title>
<link rel="stylesheet" href="https://fonts.googleapis.com/css2?family=Open+Sans:wght@400;600;700&display=swap">
<style>
  :root {
    --page-bg: #ebe8e3;
    --card-bg: #fcfcfc;
    --brand-blue: #38ade0;
    --brand-green: #1ea95b;
    --text-grey: #5a5a5a;
    --card-shadow: 0 6px 18px rgba(0,0,0,0.18);
  }
  * { margin: 0; padding: 0; box-sizing: border-box; }
  html, body {
    width: 1200px;
    height: 1062px;
    overflow: hidden;
    background: var(--page-bg);
    font-family: "Open Sans", Arial, sans-serif;
  }
  .canvas {
    position: relative;
    width: 1200px;
    height: 1062px;
  }
  .card {
    position: absolute;
    left: 220px;
    width: 760px;
    height: 434px;
    background: var(--card-bg);
    box-shadow: var(--card-shadow);
    overflow: hidden;
  }
  .card--front { top: 60px; }
  .card--back { top: 568px; }

  .edge-band {
    position: absolute;
    top: 0;
    right: 0;
    width: 64px;
    height: 100%;
  }

  .brand {
    position: absolute;
    display: flex;
    align-items: center;
    gap: 22px;
  }
  .brand__square {
    width: 92px;
    height: 92px;
    background: var(--brand-blue);
    flex: none;
  }
  .brand__name {
    font-weight: 700;
    color: var(--brand-blue);
    line-height: 1.02;
    letter-spacing: -0.5px;
  }
  .card--front .brand { left: 56px; top: 70px; }
  .card--front .brand__name { font-size: 52px; }

  .card--back .brand {
    left: 50%;
    top: 50%;
    transform: translate(-50%, -50%);
  }
  .card--back .brand__square { width: 110px; height: 110px; }
  .card--back .brand__name { font-size: 60px; }

  .contacts {
    position: absolute;
    left: 56px;
    top: 248px;
  }
  .contact { margin-bottom: 14px; }
  .contact__name {
    font-weight: 600;
    font-size: 21px;
    color: var(--brand-blue);
    line-height: 1.1;
  }
  .contact__phone {
    font-size: 16px;
    color: var(--text-grey);
    line-height: 1.3;
  }
  .contact__email {
    font-size: 16px;
    color: var(--text-grey);
    display: flex;
    align-items: center;
    gap: 8px;
    margin-top: 4px;
  }
  .contact__email-mark {
    color: var(--brand-blue);
    font-weight: 600;
    font-size: 18px;
  }
</style>
</head>
<body>
<main class="canvas">
  <section class="card card--front" aria-label="Business card front">
    <svg class="edge-band" viewBox="0 0 64 434" preserveAspectRatio="none" aria-hidden="true">
      <rect x="0" y="0" width="64" height="434" fill="var(--brand-green)"/>
      <path d="M64 0 V150 H26 Q0 150 0 125 V0 Z" fill="var(--brand-blue)"/>
      <path d="M0 125 Q0 150 26 150 H64 V162 H22 Q0 160 0 138 Z" fill="#ffffff" opacity="0.9"/>
    </svg>

    <div class="brand">
      <span class="brand__square" aria-hidden="true"></span>
      <span class="brand__name">Pale Ridge<br>Yardworks</span>
    </div>

    <div class="contacts">
      <div class="contact">
        <div class="contact__name">Dale Purvine</div>
        <div class="contact__phone">555-213-7690</div>
      </div>
      <div class="contact">
        <div class="contact__name">Martin Kolbey</div>
        <div class="contact__phone">555-864-1037</div>
      </div>
      <div class="contact__email">
        <span class="contact__email-mark">@</span>
        <span>paleridgeyardworks@mailbrook.net</span>
      </div>
    </div>
  </section>

  <section class="card card--back" aria-label="Business card back">
    <div class="brand">
      <span class="brand__square" aria-hidden="true"></span>
      <span class="brand__name">Pale Ridge<br>Yardworks</span>
    </div>
  </section>
</main>
</body>
</html>
```